Redesign Australian netball site

Existing website needs a new look and feel - http://kelvalecourts.com.au/
We require a homepage design that contains 3 sections: Chatterly feed, Recent Articles and Sponsors.
We also require a subpage design showing a main content area and a right hand sidebar (containing panels for login, chatterly feed, articles and sponsors)
Updates

Hopefully the updated brief provides more information now but if there are further questions then feel free to email me at ts@brightwharf.com.au

Reason: To allow additional submissions and design tweaks

Target Market(s)

The site needs to target parents of younger players, older players themselves and sponsors.

Requirements
Must have
• Header must contain:
1. current logo from http://kelvalecourts.com.au/
2. The slogan "Fun, Fitness, Fair Competition - Play Netball"
3. A space for a Platinum Sponsor (see current site)

Top level navigation should be:
1. Seniors
2. Juniors
3. Zippets
4. Sponsors
5. Special Offers
6. About Us
7. Umpires

```html
<!DOCTYPE html>
<html lang="en">
<head>
<meta charset="utf-8">
<title>Kelvale Netball</title>
<link rel="stylesheet" href="https://fonts.googleapis.com/css2?family=Open+Sans:ital,wght@0,400;0,600;0,700;1,400&family=PT+Sans:wght@400;700&display=swap">
<style>
:root{
  --navy:#0d2b5c;
  --navy-2:#1f4e9a;
  --pink:#e6336c;
  --pink-soft:#f05a88;
  --text:#3f3f3f;
  --muted:#7a7a7a;
  --green:#2f8a1f;
  --line:#d9d9d9;
  --gold:#f4c21b;
}
*{box-sizing:border-box;margin:0;padding:0}
html,body{width:800px;height:1200px;overflow:hidden;background:#fff}
body{position:relative;font-family:"Open Sans",sans-serif;color:var(--text)}
.abs{position:absolute}

.top-rule{left:0;top:0;width:800px;height:2px;background:var(--pink)}
.brand{left:93px;top:14px}
.brand-mark{width:40px;height:40px;border-radius:50%;background:var(--navy);margin-left:10px}
.brand-name{font-family:"PT Sans",sans-serif;font-size:13px;color:var(--navy);margin-top:24px}
.brand-tag{font-size:8px;color:#555;margin-top:3px;letter-spacing:.2px}

.util-nav{left:513px;top:12px;font-size:9px;color:var(--navy);font-weight:600}
.util-nav span{margin:0 8px}
.account{left:628px;top:2px;width:82px;height:27px;background:var(--pink);color:#fff;font-size:8.5px;font-weight:600;display:flex;align-items:center;justify-content:center;gap:5px}
.search{left:428px;top:42px;width:146px;height:24px;border:1px solid #ddd;border-radius:3px;box-shadow:0 1px 2px rgba(0,0,0,.12);font-size:7px;color:#888;padding:7px 10px}
.search svg{position:absolute;right:8px;top:6px}
.sponsor-slot{left:586px;top:42px;width:124px;height:36px;background:#e0383e;color:#fff}
.sponsor-slot .label{position:absolute;left:7px;top:8px;font-size:8px;line-height:10px}
.sponsor-slot .divider{position:absolute;left:48px;top:0;width:1px;height:36px;background:rgba(255,255,255,.45)}
.sponsor-slot .name{position:absolute;left:60px;top:7px;font-family:"PT Sans",sans-serif;font-weight:700;font-size:18px}

.main-nav{left:338px;top:81px;display:flex;font-size:9px;color:#555;height:24px;align-items:center}
.main-nav a{color:inherit;text-decoration:none;padding:0 6px;line-height:24px}
.main-nav a.active{background:var(--navy);color:#fff;border-radius:2px 2px 0 0;padding:0 8px}

.hero{left:0;top:116px;width:800px;height:322px;background:linear-gradient(180deg,#1b2340 0%,#5a3a3e 45%,#7d4a3c 100%)}
.hero-band{left:0;top:438px;width:800px;height:5px;background:var(--navy)}
.hero-title{left:143px;top:346px;font-family:"PT Sans",sans-serif;font-weight:700;font-size:25px;color:#fff;text-shadow:0 1px 3px rgba(0,0,0,.6)}
.chat-btn{left:144px;top:390px;width:118px;height:19px;background:var(--navy-2);border-radius:2px;color:#fff;font-size:7.5px;font-weight:600;display:flex;align-items:center;gap:6px;padding-left:6px}
.chat-btn i{width:10px;height:10px;background:#fff;display:block}
.hero-arrow{top:268px}
.newsletter-tab{left:0;top:254px;width:26px;height:134px;background:var(--pink-soft);border-radius:0 3px 3px 0}
.newsletter-tab span{position:absolute;left:7px;top:14px;writing-mode:vertical-rl;color:#fff;font-size:9px;letter-spacing:.5px}

.events-band{left:0;top:443px;width:800px;height:55px;background:#fff}
.events-band svg{position:absolute;left:0;top:0}
.events-title{left:112px;top:453px;color:#fff;font-family:"PT Sans",sans-serif;font-size:16px;line-height:19px}
.events-text{left:275px;top:458px;width:440px;font-size:8px;line-height:10.5px;color:#555}

.partners{left:58px;top:500px;width:684px;height:76px;background:linear-gradient(180deg,#fff 0%,#f1f1f1 50%,#fff 100%)}
.partner{position:absolute;top:28px;font-family:"PT Sans",sans-serif;font-weight:700;font-size:14px;color:#8a8a8a;display:flex;align-items:center;gap:4px}
.partner .dot{width:14px;height:14px;border-radius:50%;background:#8a8a8a}
.partner.red{color:#d8262b}

.section-title{font-family:"PT Sans",sans-serif;font-size:14px;color:var(--pink);letter-spacing:.2px}
.articles-title{left:79px;top:584px}
.article{position:absolute;left:79px;width:420px}
.rating{position:absolute;left:1px;top:0;font-size:7.5px;color:#555}
.rating b{font-weight:400;color:var(--gold);font-size:10px;letter-spacing:0}
.rating b.off{color:#888}
.article h3{position:absolute;left:138px;top:-3px;font-family:"PT Sans",sans-serif;font-weight:400;font-size:13px;color:var(--navy);white-space:nowrap}
.thumb{position:absolute;left:3px;top:19px;width:123px;height:91px;border:3px solid #fff;box-shadow:0 0 3px rgba(0,0,0,.35);background:linear-gradient(180deg,#8b8e96 0%,#b08a5c 100%)}
.article p{position:absolute;left:138px;top:22px;width:277px;font-size:7.6px;line-height:12px;font-weight:600;text-align:justify;color:#444}
.article .meta{position:absolute;left:138px;top:82px;font-size:7.6px;line-height:10px;font-style:italic;color:var(--pink);white-space:nowrap}

.ann-title{left:523px;top:584px}
.ann-arrows{left:667px;top:589px;font-size:10px;color:#aaa;letter-spacing:4px}
.ann{position:absolute;left:525px;width:166px;height:46px}
.ann .pic{position:absolute;left:0;top:0;width:32px;height:32px;border:2px solid #fff;box-shadow:0 0 2px rgba(0,0,0,.4);background:linear-gradient(135deg,#7a8fb0,#c9a48a)}
.ann .txt{position:absolute;left:40px;top:0;width:124px;font-size:7px;line-height:12px;color:#555}
.ann .when{position:absolute;right:2px;top:26px;font-size:7px;color:var(--green);font-weight:600}

.feed{left:527px;top:830px;width:164px;height:248px;background:#fff;box-shadow:0 0 2px rgba(0,0,0,.3);overflow:hidden;font-family:Arial,sans-serif}
.feed .status{height:10px;background:#2a2a2a;color:#fff;font-size:6px;display:flex;justify-content:space-between;align-items:center;padding:0 4px}
.feed .bar{height:22px;background:linear-gradient(#5b78b0,#3b5998);color:#fff;font-weight:700;font-size:13px;text-align:center;line-height:22px;position:relative}
.feed .bar i{position:absolute;top:5px;width:16px;height:12px;border-radius:2px;background:rgba(255,255,255,.25)}
.feed .input{margin:3px 3px;height:15px;border:1px solid #bbb;border-radius:8px;font-size:6.5px;color:#aaa;padding:2px 6px}
.post{position:relative;padding:2px 18px 3px 25px;border-bottom:1px solid #e3e3e3;font-size:6.3px;line-height:8px;color:#222}
.post .av{position:absolute;left:3px;top:3px;width:17px;height:17px;background:#7b7f88}
.post b{font-size:7.5px}
.post .t{position:absolute;right:20px;top:3px;font-size:6px;color:#3b5998}
.post .go{position:absolute;right:4px;top:50%;margin-top:-5px;width:11px;height:11px;border-radius:50%;background:#3b6fc8}
.feed .tabs{position:absolute;left:0;bottom:0;width:164px;height:26px;background:#222;display:flex}
.feed .tabs span{flex:1;color:#bbb;font-size:5px;text-align:center;padding-top:17px;position:relative}
.feed .tabs span::before{content:"";position:absolute;left:50%;top:5px;margin-left:-5px;width:10px;height:9px;background:#888;border-radius:2px}
.feed .tabs span.on{background:#3a3a3a;color:#fff}
.feed .tabs span.on::before{background:#5a8de0}

.footer-rule{left:58px;top:1136px;width:684px;height:1px;background:linear-gradient(90deg,#fff,#ddd 20%,#ddd 80%,#fff)}
.foot-links{left:79px;font-size:7.5px;color:#555}
.foot-links span{margin:0 4px;color:#999}
.socials{left:638px;top:1148px;display:flex;gap:4px}
.socials i{width:20px;height:20px;border-radius:50%;background:#c6c6c6;display:block}
.socials i:first-child{background:var(--navy)}
.copyright{left:573px;top:1177px;font-size:7.5px;color:#333}
.bottom-band{left:0;top:1195px;width:800px;height:5px;background:var(--navy)}
</style>
</head>
<body>
<div class="abs top-rule"></div>

<header>
  <div class="abs brand">
    <div class="brand-mark"></div>
    <div class="brand-name">Kelvale Netball</div>
    <div class="brand-tag">Fun, Fitness, Fair Competition - Play Netball</div>
  </div>
  <nav class="abs util-nav">HOME<span style="color:#999">|</span>CONTACT</nav>
  <div class="abs account">Sign Up <span>|</span> Login</div>
  <div class="abs search">Search
    <svg width="12" height="12" viewBox="0 0 12 12"><circle cx="5" cy="5" r="3.6" fill="none" stroke="#888" stroke-width="1.2"/><line x1="7.6" y1="7.6" x2="11" y2="11" stroke="#888" stroke-width="1.4"/></svg>
  </div>
  <div class="abs sponsor-slot">
    <div class="label">Platinum<br>Sponsor</div>
    <div class="divider"></div>
    <div class="name">T&amp;H</div>
  </div>
  <nav class="abs main-nav">
    <a class="active">SENIORS</a><a>JUNIORS</a><a>ZIPPETS</a><a>SPONSORS</a><a>SPECIAL OFFERS</a><a>ABOUT US</a><a>UMPIRES</a>
  </nav>
</header>

<section>
  <div class="abs hero" role="img" aria-label="Netball players leaping for the ball in a packed indoor arena"></div>
  <svg class="abs hero-arrow" style="left:74px" width="14" height="22" viewBox="0 0 14 22"><polyline points="11,2 3,11 11,20" fill="none" stroke="#fff" stroke-width="2.5"/></svg>
  <svg class="abs hero-arrow" style="left:696px" width="14" height="22" viewBox="0 0 14 22"><polyline points="3,2 11,11 3,20" fill="none" stroke="#fff" stroke-width="2.5"/></svg>
  <h1 class="abs hero-title">Fun, Fitness, Fair Competition - Play Netball</h1>
  <div class="abs chat-btn"><i></i>Sign-in with Chatterly</div>
  <div class="abs hero-band"></div>
  <div class="abs newsletter-tab"><span>SIGNUP NEWSLETTER</span></div>
</section>

<section>
  <div class="abs events-band">
    <svg width="260" height="55" viewBox="0 0 260 55"><polygon points="0,0 232,0 254,27 232,55 0,55" fill="var(--navy)"/></svg>
  </div>
  <h2 class="abs events-title">UPCOMMING<br>EVENTS</h2>
  <p class="abs events-text">Lorem ipsum dolor sit amet, consectetur adipisicing elit, sed do eiusmod tempor incididunt ut labore et dolore magna aliqua. Ut enim ad minim veniam, quis nostrud exercitation</p>
</section>

<section class="abs partners">
  <div class="partner" style="left:42px">DEALHUB</div>
  <div class="partner" style="left:126px"><span class="dot"></span>savenet</div>
  <div class="partner" style="left:220px">ThriftPoint</div>
  <div class="partner" style="left:327px">bluepost</div>
  <div class="partner red" style="left:405px"><span class="dot" style="background:#d8262b"></span>Keenly</div>
  <div class="partner" style="left:496px">CartWise</div>
</section>

<section>
  <h2 class="abs section-title articles-title">RECENT ARTICLES</h2>

  <article class="article" style="top:612px">
    <div class="rating">Clients Rating : <b>★★★★</b><b class="off">★</b></div>
    <h3>Clara Whitfield Clinic for KN Members</h3>
    <div class="thumb" role="img" aria-label="Players contesting the ball on an indoor court"></div>
    <p>Lorem Ipsum is simply dummy text of the printing and typesetting industry. Lorem Ipsum has been the industry's standard dummy text ever since the 1500s, when an unknown printer took a galley of type and scrambled it to make a type specimen book.</p>
    <div class="meta">Saturday 11th May 2013 | Harlow Rd Courts, Kelvale | Time: 2.00pm- 5.00pm<br>Cost: $45 per child; includes coaching and a goodies bag!</div>
  </article>

  <article class="article" style="top:739px">
    <div class="rating">Clients Rating : <b>★★★★</b><b class="off">★</b></div>
    <h3>Clara Whitfield Clinic for KN Members</h3>
    <div class="thumb" role="img" aria-label="Player holding the ball while defenders close in"></div>
    <p>Lorem Ipsum is simply dummy text of the printing and typesetting industry. Lorem Ipsum has been the industry's standard dummy text ever since the 1500s, when an unknown printer took a galley of type and scrambled it to make a type specimen book.</p>
    <div class="meta">Saturday 11th May 2013 | Harlow Rd Courts, Kelvale | Time: 2.00pm- 5.00pm<br>Cost: $45 per child; includes coaching and a goodies bag!</div>
  </article>

  <article class="article" style="top:869px">
    <div class="rating">Clients Rating : <b>★★★★</b><b class="off">★</b></div>
    <h3>Clara Whitfield Clinic for KN Members</h3>
    <div class="thumb" role="img" aria-label="Junior players in red and black during a match"></div>
    <p>Lorem Ipsum is simply dummy text of the printing and typesetting industry. Lorem Ipsum has been the industry's standard dummy text ever since the 1500s, when an unknown printer took a galley of type and scrambled it to make a type specimen book.</p>
    <div class="meta">Saturday 11th May 2013 | Harlow Rd Courts, Kelvale | Time: 2.00pm- 5.00pm<br>Cost: $45 per child; includes coaching and a goodies bag!</div>
  </article>

  <article class="article" style="top:994px">
    <div class="rating">Clients Rating : <b>★★★★</b><b class="off">★</b></div>
    <h3>Clara Whitfield Clinic for KN Members</h3>
    <div class="thumb" role="img" aria-label="Player passing the ball in an arena"></div>
    <p>Lorem Ipsum is simply dummy text of the printing and typesetting industry. Lorem Ipsum has been the industry's standard dummy text ever since the 1500s, when an unknown printer took a galley of type and scrambled it to make a type specimen book.</p>
    <div class="meta">Saturday 11th May 2013 | Harlow Rd Courts, Kelvale | Time: 2.00pm- 5.00pm<br>Cost: $45 per child; includes coaching and a goodies bag!</div>
  </article>
</section>

<aside>
  <h2 class="abs section-title ann-title">ANNOUNCEMENTS</h2>
  <div class="abs ann-arrows">‹ ›</div>

  <div class="ann" style="top:620px"><div class="pic" role="img" aria-label="Member photo"></div><div class="txt">Ben R. commented on Need some Computer / IT help "Hi will you raise your offe..."</div><div class="when">5 Hours ago!</div></div>
  <div class="ann" style="top:674px"><div class="pic" role="img" aria-label="Member photo"></div><div class="txt">Ben R. commented on Need some Computer / IT help "Hi will you raise your offe..."</div><div class="when">5 Hours ago!</div></div>
  <div class="ann" style="top:722px"><div class="pic" role="img" aria-label="Member photo"></div><div class="txt">Ben R. commented on Need some Computer / IT help "Hi will you raise your offe..."</div><div class="when">5 Hours ago!</div></div>
  <div class="ann" style="top:776px"><div class="pic" role="img" aria-label="Member photo"></div><div class="txt">Ben R. commented on Need some Computer / IT help "Hi will you raise your offe..."</div><div class="when">5 Hours ago!</div></div>

  <div class="abs feed">
    <div class="status"><span>Telvo</span><span>9:39 PM</span><span>▮▮</span></div>
    <div class="bar"><i style="left:5px"></i>chatterly<i style="right:5px"></i></div>
    <div class="input">What are you doing?</div>
    <div class="post"><div class="av"></div><b>Tom Ashcroft</b><span class="t">4:52 PM</span><br>my trio will be playing on the rooftop at the Foundry in Bayside tomorrow 5-7p - join us for drink and some killer guitar tones :-).<span class="go"></span></div>
    <div class="post"><div class="av"></div><b>Nina Vale</b><span class="t">4:47 PM</span><br>Writing up some answers for a reporter from the Harbour Gazette (thanks @jordanreef for the referral!)<span class="go"></span></div>
    <div class="post"><div class="av"></div><b>Owen Marsh</b><span class="t">4:44 PM</span><br>is on the road again...<span class="go"></span></div>
    <div class="post"><div class="av"></div><b>Rhys Calder</b><span class="t">4:38 PM</span><br>Big fan of Lantern Fields. Quiet Harbour seems good.<span class="go"></span></div>
    <div class="tabs"><span class="on">Home</span><span>Profile</span><span>Friends</span><span>Chat</span><span>Inbox</span></div>
  </div>
</aside>

<footer>
  <div class="abs footer-rule"></div>
  <div class="abs foot-links" style="top:1153px">Home<span>|</span>Seniors<span>|</span>Juniors<span>|</span>Zippets<span>|</span>Sponsors<span>|</span>Special Offers<span>|</span>About Us<span>|</span>Umpires<span>|</span>Contact Us<span>|</span>Members Area<span>|</span>Articles</div>
  <div class="abs foot-links" style="top:1171px">Club Informations<span>|</span>2013 Competition Ladders<span>|</span>Events Calendar<span>|</span>Upcoming Events</div>
  <div class="abs socials"><i></i><i></i><i></i></div>
  <div class="abs copyright">© 2013 &nbsp; www.kelvalecourts.com.au</div>
  <div class="abs bottom-band"></div>
</footer>
</body>
</html>
```